KVRo Business Cards

We need a business card design. We are a Technology (Audio Visual) design, sales and installation company. Looking for a double sided design, clean

Contact Information for Business Card

Clean, modern look, 2 sided

Font styles to use
Sans Serif

```html
<!DOCTYPE html>
<html lang="en">
<head>
<meta charset="utf-8">
<title>KVRo Business Cards</title>
<link rel="stylesheet" href="https://fonts.googleapis.com/css2?family=Montserrat:wght@500;600;700&family=Roboto:wght@400&display=swap">
<style>
  :root {
    --backdrop: #97a7b2;
    --navy: #1d3242;
    --orange: #f39325;
    --paper: #ffffff;
    --ink: #2b2b2b;
  }
  * { margin: 0; padding: 0; box-sizing: border-box; }
  html, body { width: 720px; height: 1200px; overflow: hidden; }
  body {
    background: var(--backdrop);
    font-family: "Montserrat", sans-serif;
    display: flex;
    flex-direction: column;
    align-items: center;
    justify-content: center;
    gap: 0;
  }
  .sheet { width: 504px; }
  .sheet-title {
    font-family: "Roboto", sans-serif;
    font-weight: 400;
    font-size: 24px;
    color: var(--ink);
    margin: 0 0 32px -2px;
    white-space: nowrap;
  }
  .card { position: relative; width: 504px; height: 288px; overflow: hidden; }
  .card-front { background: var(--paper); }
  .card-back { background: var(--navy); margin-top: 22px; }

  .holder { position: absolute; left: 80px; top: 44px; color: var(--navy); }
  .holder-name { font-weight: 700; font-size: 20px; line-height: 1.1; letter-spacing: 0.2px; }
  .holder-role { font-weight: 600; font-size: 13.5px; margin-top: 2px; padding-left: 1px; }

  .contact-list { position: absolute; left: 0; top: 95px; list-style: none; }
  .contact-item { display: flex; align-items: center; height: 33px; margin-bottom: 3px; }
  .contact-icon {
    width: 65px; height: 33px; background: var(--orange);
    display: flex; align-items: center; justify-content: center;
    padding-left: 14px;
  }
  .contact-text { margin-left: 15px; font-weight: 500; font-size: 12.5px; color: var(--navy); letter-spacing: 0.3px; }

  .wordmark { position: absolute; font-weight: 700; letter-spacing: -2px; line-height: 1; }
  .card-front .wordmark { right: 62px; top: 36px; font-size: 70px; color: var(--navy); }
  .card-back .wordmark { left: 0; right: 0; top: 96px; text-align: center; font-size: 82px; color: var(--paper); }

  .footer-band { position: absolute; left: 0; bottom: 0; }
  .back-url {
    position: absolute; left: 0; right: 0; top: 210px; text-align: center;
    color: var(--paper); font-weight: 500; font-size: 19px; letter-spacing: 0.3px;
  }
</style>
</head>
<body>
  <main class="sheet">
    <h1 class="sheet-title">Business Card: Dimensions&nbsp; 3.5" x 2.0"</h1>

    <section class="card card-front" aria-label="Card front">
      <div class="holder">
        <p class="holder-name">Owner’s Name</p>
        <p class="holder-role">Designation</p>
      </div>

      <ul class="contact-list">
        <li class="contact-item">
          <span class="contact-icon">
            <svg width="12" height="18" viewBox="0 0 12 18" aria-hidden="true"><rect x="1" y="1" width="10" height="16" rx="1.5" fill="none" stroke="#fff" stroke-width="1.4"/><line x1="5" y1="14.5" x2="7" y2="14.5" stroke="#fff" stroke-width="1.4"/></svg>
          </span>
          <span class="contact-text">555-014-7720 - dummy no.</span>
        </li>
        <li class="contact-item">
          <span class="contact-icon">
            <svg width="16" height="11" viewBox="0 0 16 11" aria-hidden="true"><rect x="0.5" y="0.5" width="15" height="10" fill="#fff"/><path d="M1 1 L8 6.5 L15 1 M1 10 L6 5.5 M15 10 L10 5.5" fill="none" stroke="#f39325" stroke-width="1"/></svg>
          </span>
          <span class="contact-text">info@kvro.com</span>
        </li>
        <li class="contact-item">
          <span class="contact-icon">
            <svg width="17" height="17" viewBox="0 0 17 17" aria-hidden="true"><g fill="none" stroke="#fff" stroke-width="1.3"><circle cx="8.5" cy="8.5" r="7.5"/><ellipse cx="8.5" cy="8.5" rx="3.3" ry="7.5"/><line x1="1" y1="8.5" x2="16" y2="8.5"/><line x1="2.3" y1="4.6" x2="14.7" y2="4.6"/><line x1="2.3" y1="12.4" x2="14.7" y2="12.4"/></g></svg>
          </span>
          <span class="contact-text">www.kvro.com</span>
        </li>
        <li class="contact-item">
          <span class="contact-icon">
            <svg width="12" height="17" viewBox="0 0 12 17" aria-hidden="true"><path d="M6 0.5 C2.9 0.5 0.5 2.9 0.5 5.9 C0.5 9.8 6 16.5 6 16.5 C6 16.5 11.5 9.8 11.5 5.9 C11.5 2.9 9.1 0.5 6 0.5 Z" fill="#fff"/><circle cx="6" cy="5.9" r="2.1" fill="#f39325"/></svg>
          </span>
          <span class="contact-text">Company address and or branch address</span>
        </li>
      </ul>

      <div class="wordmark">KVRo</div>

      <svg class="footer-band" width="504" height="33" viewBox="0 0 504 33" aria-hidden="true">
        <polygon points="0,0 254,0 232,33 0,33" fill="var(--navy)"/>
        <polygon points="262,0 504,0 504,33 240,33" fill="var(--orange)"/>
      </svg>
    </section>

    <section class="card card-back" aria-label="Card back">
      <div class="wordmark">KVRo</div>
      <p class="back-url">www.kvro.com</p>
    </section>
  </main>
</body>
</html>
```